Functional Beverage Bottle Labele

I need a label created for a functional beverage. A functional beverage is a drink that provides a function as well as being a beverage. This drink aims to help ease stress and allow women to relax at the end of their day. It has been designed specifically with women in mind (men can also drink it though).

The brand values are:
Natural - we use nature to nurture our best selves, Nourishing - in the ingredients we use and messages we share, Nimble - in the way we respond to our customers and operate on a daily basis

I am looking for a modern, clean looking label. The label will be going on to a clear 330ml flint ROPP bottle, with a silver ROPP cap and contains a light pink liquid. I have attached a mock up for you to see the colour of the liquid and the style of the bottle.

I have included further information in the design brief, colour palette, logo and other items to assist you with the process of designing the label. Happy to answer any questions. I am based in Melbourne Australia.

I have uploaded the files individually and as a zip file.

Target Market(s)

Australian females aged from 21 - 60

Font styles to use
Serif
Sans Serif
Decorative
Script

Requirements
Must have
• Required on the front of the label:

Brand Logo - attached

Drink function - the function of this drink is RELAX. There will be two others in the product line, REVIVE and RECOVER. Please include RELAX somewhere on the front.

Drink flavour
Native Strawberry Gum

Drink measurement
330mL

Product description
Sparkling water with adaptogens to help you adapt to life stressors

Key call outs - 100% natural, Sugar free

There are other requirements for the remainder of the label that I have included in the document attached.
Nice to have
• Please feel free to add icons, lines, etc to make the design the best it can be and give it some personality.

The map of Victoria that I have asked to be included should not be on the front and it should be no bigger than the barcode.
Should not have
• UPDATED: There should be no strawberry images on the bottle. The Native Strawberry Gum flavour comes from the leaves of a type of eucalyptus tree grown in Australia. I have added a photo of the leaves.

```html
<!DOCTYPE html>
<html lang="en">
<head>
<meta charset="utf-8">
<title>LUMA drinks – Relax label</title>
<link rel="stylesheet" href="https://fonts.googleapis.com/css2?family=Bodoni+Moda:wght@700&family=Raleway:wght@200;300&family=Roboto+Condensed:wght@400;700&display=swap">
<style>
  :root {
    --backdrop: #d9d6d4;
    --pink-light: #f3c3d3;
    --pink: #e6a4bf;
    --lilac: #b89bd2;
    --sky: #6fa3da;
    --periwinkle: #7d8fcf;
    --violet: #8a7cc0;
    --white: #ffffff;
    --rule-pink: #f1b6c9;
    --leaf: #f0a9bd;
  }
  * { margin: 0; padding: 0; box-sizing: border-box; }
  html, body {
    width: 1200px;
    height: 2419px;
    overflow: hidden;
    background: var(--backdrop);
  }
  .label {
    position: absolute;
    left: 100px;
    top: 460px;
    width: 1000px;
    height: 1500px;
    background:
      linear-gradient(90deg, rgba(111,163,218,0.35) 0%, rgba(111,163,218,0) 40%, rgba(138,124,192,0) 60%, rgba(138,124,192,0.45) 100%),
      linear-gradient(180deg,
        var(--pink-light) 0%,
        var(--lilac) 9%,
        var(--sky) 28%,
        var(--periwinkle) 62%,
        var(--lilac) 80%,
        var(--pink-light) 90%,
        var(--pink) 100%);
  }
  .label-art {
    position: absolute;
    inset: 0;
    width: 1000px;
    height: 1500px;
  }
  .brand-name {
    font-family: "Raleway", sans-serif;
    font-weight: 200;
    fill: var(--white);
  }
  .function-name {
    font-family: "Bodoni Moda", serif;
    font-weight: 700;
    fill: var(--white);
  }
  .description, .callout, .flavour {
    font-family: "Roboto Condensed", sans-serif;
    font-weight: 700;
    fill: var(--white);
  }
  .callout-small { fill: var(--white); font-family: "Roboto Condensed", sans-serif; font-weight: 700; }
  .volume {
    font-family: "Raleway", sans-serif;
    font-weight: 300;
    fill: var(--white);
  }
  .frame { fill: none; stroke: var(--white); stroke-width: 4; }
  .rule { stroke: var(--rule-pink); stroke-width: 2; }
  .rule-dot { fill: var(--rule-pink); }
</style>
</head>
<body>
  <div class="label">
    <svg class="label-art" viewBox="0 0 1000 1500" xmlns="http://www.w3.org/2000/svg">
      <!-- frame with openings for brand and flavour -->
      <path class="frame" d="M248 238 H76 Q46 238 46 268 V1218 Q46 1248 76 1248 H198"/>
      <path class="frame" d="M772 238 H920 Q950 238 950 268 V1218 Q950 1248 920 1248 H790"/>

      <!-- brand -->
      <text class="brand-name" x="508" y="290" font-size="104" text-anchor="middle" letter-spacing="6">LUMA</text>
      <text class="brand-name" x="508" y="352" font-size="32" text-anchor="middle" letter-spacing="5">drinks</text>

      <!-- function -->
      <text class="function-name" x="495" y="822" font-size="600" text-anchor="middle" textLength="772" lengthAdjust="spacingAndGlyphs">RELAX</text>

      <!-- description rules -->
      <line class="rule" x1="150" y1="857" x2="812" y2="857"/>
      <circle class="rule-dot" cx="139" cy="857" r="4"/>
      <circle class="rule-dot" cx="823" cy="857" r="4"/>
      <line class="rule" x1="150" y1="972" x2="812" y2="972"/>
      <circle class="rule-dot" cx="139" cy="972" r="4"/>
      <circle class="rule-dot" cx="823" cy="972" r="4"/>

      <text class="description" x="481" y="913" font-size="34" text-anchor="middle" textLength="594" lengthAdjust="spacingAndGlyphs">SPARKLING WATER WITH ADAPTOGENS</text>
      <text class="description" x="481" y="957" font-size="34" text-anchor="middle" textLength="634" lengthAdjust="spacingAndGlyphs">TO HELP YOU ADAPT TO LIFE STRESSORS</text>

      <!-- key call outs -->
      <text class="callout" x="280" y="1108" font-size="104" textLength="136" lengthAdjust="spacingAndGlyphs">100</text>
      <text class="callout" x="418" y="1058" font-size="50" textLength="230" lengthAdjust="spacingAndGlyphs">%NATURAL</text>
      <line x1="448" y1="1066" x2="648" y2="1066" stroke="#ffffff" stroke-width="3"/>
      <text class="callout-small" x="448" y="1104" font-size="34" textLength="200" lengthAdjust="spacingAndGlyphs" letter-spacing="2">SUGAR FREE</text>
      <line x1="448" y1="1112" x2="648" y2="1112" stroke="#ffffff" stroke-width="3"/>

      <!-- flavour leaf -->
      <ellipse role="img" aria-label="Strawberry gum leaf" cx="490" cy="1164" rx="130" ry="28" fill="var(--leaf)"/>

      <!-- flavour arc -->
      <defs>
        <path id="flavour-arc" d="M180 1150 A380 380 0 0 0 820 1150"/>
      </defs>
      <text class="flavour" font-size="34" letter-spacing="1">
        <textPath href="#flavour-arc" startOffset="50%" text-anchor="middle">•  NATIVE STRAWBERRY GUM  •</textPath>
      </text>

      <!-- volume -->
      <text class="volume" x="500" y="1422" font-size="46" text-anchor="middle">330ml</text>
    </svg>
  </div>
</body>
</html>
```